Export company based in South America (Ecuador) we export flowers, chocolate, and bananas

We need a website that gives our potential clients and introduction into our company and the different types of commodities we export around the world. We are based in Quito, Ecuador so the website should portray the feel of Ecuadorian landscapes within a modern looking website.
At the moment we are exporting roses, chocolate, and bananas so the website should have an intro to our company and then three different areas that describe our three main commodity. The three different sections should explain why each of the products from Ecuador are some of the best in the world in their categories and the benefits of importing the commodity through our company.
Industry/Entity Type
Commodity
Number of Pages Required
4 page

```html
<!DOCTYPE html>
<html lang="en">
<head>
<meta charset="utf-8">
<title>Altavera Export</title>
<link href="https://fonts.googleapis.com/css2?family=Noto+Serif:wght@400;700&family=Lato:wght@400;700&display=swap" rel="stylesheet">
<style>
:root{
  --teal:#1f7a71;
  --ink:#2b2b2b;
  --text:#4a4a4a;
  --grey:#efefef;
  --line:#c9c9c9;
  --footer:#1c1c1c;
  --footer-deep:#121212;
  --white:#ffffff;
}
*{box-sizing:border-box;margin:0;padding:0}
html,body{width:1200px;height:4559px;overflow:hidden}
body{background:var(--white);font-family:"Lato",sans-serif;color:var(--text)}
h1,h2,h3,.brand{font-family:"Noto Serif",serif;color:var(--ink)}
.btn{display:inline-block;background:var(--teal);color:var(--white);font-family:"Noto Serif",serif;font-size:18px;padding:12px 0;width:191px;text-align:center;text-decoration:none}

/* nav */
.nav{height:90px;position:relative}
.nav a{font-family:"Noto Serif",serif;font-size:16px;color:var(--ink);text-decoration:none;position:absolute;top:34px}
.nav .active{background:var(--teal);color:var(--white);padding:5px 18px;top:29px;left:101px}
.nav .brand{position:absolute;left:0;width:1200px;text-align:center;top:14px;font-size:50px;font-weight:700;pointer-events:none}

/* hero */
.hero{height:611px;position:relative;background:linear-gradient(180deg,#9bb4c8 0%,#6a7f86 22%,#2f6f86 42%,#3e8a74 58%,#8a6a3e 76%,#c98a3a 100%)}
.hero h1{position:absolute;top:188px;width:100%;text-align:center;color:var(--white);font-size:68px;line-height:70px;font-weight:700}
.dots{position:absolute;top:553px;left:0;width:100%;display:flex;justify-content:center;gap:18px}
.dots span{width:14px;height:14px;border-radius:50%;background:var(--white)}
.dots span:first-child{background:var(--teal)}

/* intro */
.intro{height:481px;text-align:center;padding-top:64px}
.intro h2{font-size:34px}
.intro p{width:840px;margin:26px auto 0;font-size:16px;line-height:30px}
.cards{display:flex;gap:30px;justify-content:center;margin-top:42px}
.card{width:331px;height:195px;border:2px solid var(--line);display:flex;flex-direction:column;align-items:center;justify-content:center;gap:22px}
.card h3{color:var(--teal);font-size:29px}
.icon{width:76px;height:76px;border-radius:8px}

/* about */
.band{background:var(--grey);height:464px;position:relative}
.frame{position:absolute;background:var(--white);border:1px solid var(--line);padding:6px}
.frame .inner{border:2px solid #888;height:100%;text-align:center;padding:38px 20px 0}
.frame h2{font-size:34px}
.frame p{font-size:16px;line-height:30px;margin:14px 0 24px}
.photo{position:absolute}

/* split rows */
.split{display:flex;height:481px}
.split .half{width:600px;height:481px}
.split .copy{text-align:center;padding-top:150px}
.split .copy h2{font-size:34px}
.split .copy p{width:420px;margin:18px auto 40px;font-size:16px;line-height:30px}

.gap{height:70px}

/* benefits */
.benefits{height:522px;text-align:center;padding-top:50px}
.benefits h2{font-size:38px}
.bgrid{display:flex;gap:30px;justify-content:center;margin-top:30px}
.bitem{width:331px}
.bitem .pic{height:195px}
.bitem h3{color:var(--teal);font-size:23px;font-weight:400;margin-top:36px}
.bitem p{font-size:16px;line-height:28px;margin-top:8px}

/* footer */
.footer{background:var(--footer);height:282px;position:relative;color:#e6e6e6}
.footer .col{position:absolute;top:52px;font-size:13px;line-height:27px}
.footer h4{font-family:"Noto Serif",serif;font-weight:400;font-size:22px;color:var(--white);line-height:30px;margin-bottom:6px}
.footer .brand{color:#bdbdbd;font-size:42px;line-height:44px;margin-bottom:8px;font-weight:700}
.footer .logo-col{top:40px;line-height:26px}
.footer ul{list-style:none}
.email{width:241px;height:38px;background:var(--white);color:#333;font-size:13px;padding:10px 12px}
.sub{display:block;margin:16px 0 0 141px;width:100px;background:var(--teal);color:var(--white);font-family:"Noto Serif",serif;font-weight:700;font-size:15px;text-align:center;padding:6px 0}
.bottom{background:var(--footer-deep);height:61px;display:flex;align-items:center;justify-content:space-between;padding:0 70px 0 77px;color:#bbb;font-size:12px}
.social{display:flex;gap:26px}
.social span{width:18px;height:18px;border-radius:50%;background:#e6e6e6}
</style>
</head>
<body>

<header class="nav">
  <a class="active" href="#">Home</a>
  <a href="#" style="left:215px">About Us</a>
  <a href="#" style="left:338px">Services</a>
  <div class="brand">Altavera</div>
  <a href="#" style="left:794px">Why Us</a>
  <a href="#" style="left:905px">Blog</a>
  <a href="#" style="left:988px">Contact Us</a>
</header>

<section class="hero" role="img" aria-label="Coastal volcanic island landscape with turquoise bays and a rocky pinnacle">
  <h1>Welcome to<br>Altavera</h1>
  <div class="dots"><span></span><span></span><span></span></div>
</section>

<section class="intro">
  <h2>What We Do</h2>
  <p>Quisque eu enim laoreet, hendrerit tellus et, lobortis diam. Interdum et malesuada fames ac ante ipsum primis in faucibus nascetur ridiculus mus ultricies maximus.</p>
  <div class="cards">
    <div class="card">
      <div class="icon" role="img" aria-label="Flower icon" style="background:linear-gradient(180deg,#e0a0a0,#c9d6c0)"></div>
      <h3>Flowers</h3>
    </div>
    <div class="card">
      <div class="icon" role="img" aria-label="Chocolate icon" style="background:linear-gradient(180deg,#c9a58a,#ead3a0)"></div>
      <h3>Chocolate</h3>
    </div>
    <div class="card">
      <div class="icon" role="img" aria-label="Banana icon" style="background:linear-gradient(180deg,#f0d890,#e8c870)"></div>
      <h3>Bananas</h3>
    </div>
  </div>
</section>

<section class="band">
  <div class="frame" style="left:74px;top:50px;width:331px;height:363px">
    <div class="inner">
      <h2>About Altavera</h2>
      <p>Quisque eu enim laoreet, hendrerit tellus et, lobortis diam. Interdum et malesuada fames ac ante ipsum primis in faucibus nascetur ridiculus mus ultricies maximus.</p>
      <a class="btn" href="#">Read More</a>
    </div>
  </div>
  <div class="photo" role="img" aria-label="Andean highland farmland with a field of red and purple flowering crops" style="left:434px;top:50px;width:693px;height:363px;background:linear-gradient(180deg,#6f8fb8 0%,#6d7a6a 22%,#3f6a3a 40%,#a6643e 60%,#b3503f 80%,#8a4a3a 100%)"></div>
</section>

<div class="gap"></div>

<section class="split">
  <div class="half" role="img" aria-label="Field of pink and purple cosmos flowers" style="background:linear-gradient(135deg,#b9c9a0 0%,#a67ab8 35%,#8a4e9a 60%,#6e8a4a 100%)"></div>
  <div class="half copy">
    <h2>Flowers</h2>
    <p>Lorem ipsum dolor sit amet, consectetur adipiscing elit. Aliquam tincidunt, massa a scelerisque finibus, est lectus tempor erat, eget tempor libero lorem sit amet dolor.</p>
    <a class="btn" href="#">Read More</a>
  </div>
</section>
<section class="split">
  <div class="half copy">
    <h2>Chocolate</h2>
    <p>Lorem ipsum dolor sit amet, consectetur adipiscing elit. Aliquam tincidunt, massa a scelerisque finibus, est lectus tempor erat, eget tempor libero lorem sit amet dolor.</p>
    <a class="btn" href="#">Read More</a>
  </div>
  <div class="half" role="img" aria-label="Broken dark chocolate pieces with cocoa nibs on a black background" style="background:radial-gradient(ellipse at 65% 65%,#4a2a20 0%,#241410 35%,#080808 70%)"></div>
</section>
<section class="split">
  <div class="half" role="img" aria-label="Bunch of ripening bananas hanging among green banana leaves" style="background:radial-gradient(ellipse at 40% 50%,#d7b24a 0%,#9ac23a 35%,#3d8a20 70%,#2a5a18 100%)"></div>
  <div class="half copy">
    <h2>Bananas</h2>
    <p>Lorem ipsum dolor sit amet, consectetur adipiscing elit. Aliquam tincidunt, massa a scelerisque finibus, est lectus tempor erat, eget tempor libero lorem sit amet dolor.</p>
    <a class="btn" href="#">Read More</a>
  </div>
</section>

<div class="gap"></div>

<section class="band" style="height:466px">
  <div class="photo" role="img" aria-label="Warehouse workers in high-visibility vests handling boxes on shelves" style="left:74px;top:50px;width:693px;height:363px;background:linear-gradient(90deg,#8a6a4a 0%,#d2c23a 30%,#9a8a6a 55%,#c8b87a 80%,#a89a8a 100%)"></div>
  <div class="frame" style="left:797px;top:50px;width:330px;height:363px">
    <div class="inner">
      <h2>Why Choose Us</h2>
      <p>Quisque eu enim laoreet, hendrerit tellus et, lobortis diam. Interdum et malesuada fames ac ante ipsum primis in faucibus nascetur ridiculus mus ultricies maximus.</p>
      <a class="btn" href="#">Read More</a>
    </div>
  </div>
</section>

<section class="benefits">
  <h2>Benefits</h2>
  <div class="bgrid">
    <div class="bitem">
      <div class="pic" role="img" aria-label="Rows of banana bunches in a packing facility" style="background:linear-gradient(180deg,#4a4a3a 0%,#c8a43a 45%,#8a7a2a 100%)"></div>
      <h3>Morbi Tempor</h3>
      <p>Quisque eu enim laoreet, hendrerit tellus et, lobortis diam. Interdum et malesuada fames ac ante.</p>
    </div>
    <div class="bitem">
      <div class="pic" role="img" aria-label="Gloved hand arranging chocolates on a production line" style="background:linear-gradient(135deg,#c8c0b8 0%,#a07ab8 45%,#5a3a2a 75%,#3a2418 100%)"></div>
      <h3>Morbi Tempor</h3>
      <p>Quisque eu enim laoreet, hendrerit tellus et, lobortis diam. Interdum et malesuada fames ac ante.</p>
    </div>
    <div class="bitem">
      <div class="pic" role="img" aria-label="Crates of fresh flowers in a cold storage warehouse" style="background:linear-gradient(135deg,#5a5a5a 0%,#8ab04a 35%,#b84a4a 60%,#3a3a3a 100%)"></div>
      <h3>Morbi Tempor</h3>
      <p>Quisque eu enim laoreet, hendrerit tellus et, lobortis diam. Interdum et malesuada fames ac ante.</p>
    </div>
  </div>
</section>

<footer>
  <div class="footer">
    <div class="col logo-col" style="left:74px;width:260px">
      <div class="brand">Altavera</div>
      <p>Cras venenatis urna id augue ultrices consectetur. Mauris malesuada dolor in feugiat viverra augue orci ullamcorper urna, aliquet tincidunt</p>
    </div>
    <div class="col" style="left:405px">
      <h4>Site Map</h4>
      <ul><li>Home</li><li>About Us</li><li>Services</li><li>Why Us</li><li>Blog</li><li>Contac tUs</li></ul>
    </div>
    <div class="col" style="left:626px">
      <h4>Get in touch</h4>
      <p>48 Meridian Ave, Ste 310,<br>Quito 170135.<br>1-800-555-0142<br>hello@altavera-export.com</p>
    </div>
    <div class="col" style="left:885px">
      <h4>Newsletter</h4>
      <div class="email">Email Address</div>
      <span class="sub">Sign Up</span>
    </div>
  </div>
  <div class="bottom">
    <span>Copyright © 2020 Altavera Export All Rights Reserved</span>
    <div class="social"><span></span><span></span><span></span><span></span><span></span></div>
  </div>
</footer>

</body>
</html>
```